Paperback Book Cover Design

I need a professional cover designed for my new book. You must use the design template enclosed. The title of the book is “Open Your Digital Purse Now!” The graphic used on the book cover should of course relate to making money online through various skills such as writing, graphic design, online marketing, photography, trading, Tradlo etc. The graphic(s) used must demonstrate to the reader that the book gives various ways to make money online.

At the top of the book you must include the sub heading “Earn From Home Collection”. The main title of the book is “Open Your Digital Purse Now!”, which of course should be highly prominent on the front cover. The front cover must also include the author name, Gerald Whitcombe.

I have no preference to colours used so do be creative to create an eye catching cover design.

The spine of the book should include the main title and the author name. Feel free to use an image or images for the rear of the book and just add dummy text.

The winning designer must supply a layered psd file complete with all fonts and elements used.

Industry/Entity Type

Graphic Design

Requirements
Must have
• The winning designer must supply a layered psd file complete with all fonts and elements used.

```html
<!DOCTYPE html>
<html lang="en">
<head>
<meta charset="utf-8">
<title>Open Your Digital Purse Now! – Cover</title>
<link rel="stylesheet" href="https://fonts.googleapis.com/css2?family=Open+Sans:wght@600;700;800&display=swap">
<style>
  :root {
    --page-bg: #ffffff;
    --band-black: #0b0b0b;
    --band-black-soft: #262626;
    --cover-blue: #4a8ee0;
    --cover-blue-deep: #1f4f9c;
    --tile-frame: #ffffff;
    --tile-edge: #c9d3de;
    --art-light: #e8eef6;
    --art-mid: #8fb1d8;
    --art-warm: #e9c48c;
    --text-light: #ffffff;
  }
  * { box-sizing: border-box; margin: 0; padding: 0; }
  html, body {
    width: 1200px;
    height: 1000px;
    overflow: hidden;
    background: var(--page-bg);
  }
  .canvas {
    width: 1200px;
    height: 1000px;
    display: flex;
    align-items: center;
    justify-content: center;
  }
  .book-cover {
    width: 640px;
    height: 880px;
    display: flex;
    flex-direction: column;
    font-family: "Open Sans", Arial, sans-serif;
    color: var(--text-light);
    box-shadow: 0 10px 30px rgba(0,0,0,0.25);
  }
  .title-band {
    height: 270px;
    background: linear-gradient(180deg, var(--band-black) 0%, var(--band-black-soft) 100%);
    display: flex;
    align-items: center;
    justify-content: center;
    text-align: center;
    text-transform: uppercase;
  }
  .book-title { line-height: 1.06; }
  .title-lead { display: block; font-size: 44px; font-weight: 700; }
  .title-main { display: block; font-size: 68px; font-weight: 700; }
  .artwork-panel {
    flex: 1;
    position: relative;
    overflow: hidden;
    background: radial-gradient(ellipse at 50% 30%, var(--cover-blue) 0%, var(--cover-blue-deep) 100%);
  }
  .skill-tile {
    position: absolute;
    padding: 9px;
    background: var(--tile-frame);
    border: 1px solid var(--tile-edge);
    box-shadow: 2px 4px 8px rgba(0,0,0,0.35);
  }
  .skill-art {
    width: 100%;
    height: 100%;
    background: linear-gradient(150deg, var(--art-light) 0%, var(--art-mid) 70%, var(--art-warm) 100%);
  }
  .tile-reflection {
    position: absolute;
    top: 470px;
    width: 108px;
    height: 50px;
    border: 2px solid rgba(255,255,255,0.12);
    background: rgba(255,255,255,0.06);
  }
  .series-name {
    position: absolute;
    right: 34px;
    bottom: 28px;
    font-size: 21px;
    font-weight: 600;
    text-transform: uppercase;
  }
  .author-band {
    height: 72px;
    background: var(--band-black);
    display: flex;
    align-items: center;
    justify-content: center;
    font-size: 29px;
    font-weight: 800;
    letter-spacing: 1.5px;
    text-transform: uppercase;
  }
</style>
</head>
<body>
  <main class="canvas">
    <article class="book-cover">
      <header class="title-band">
        <h1 class="book-title">
          <span class="title-lead">Open Your</span>
          <span class="title-main">Digital Purse</span>
          <span class="title-main">Now!</span>
        </h1>
      </header>
      <section class="artwork-panel">
        <div class="skill-tile" style="left:120px;top:94px;width:104px;height:100px"><div class="skill-art" role="img" aria-label="Painting easel icon for art and illustration"></div></div>
        <div class="skill-tile" style="left:233px;top:37px;width:104px;height:100px"><div class="skill-art" role="img" aria-label="Map and brochure icon for print design"></div></div>
        <div class="skill-tile" style="left:348px;top:68px;width:104px;height:100px"><div class="skill-art" role="img" aria-label="Pen over document icon for writing"></div></div>
        <div class="skill-tile" style="left:515px;top:55px;width:108px;height:108px"><div class="skill-art" role="img" aria-label="Parcel and disc icon for selling products"></div></div>
        <div class="skill-tile" style="left:33px;top:163px;width:104px;height:100px"><div class="skill-art" role="img" aria-label="Payment cards icon for online payments"></div></div>
        <div class="skill-tile" style="left:158px;top:187px;width:86px;height:84px"><div class="skill-art" role="img" aria-label="Checklist notepad icon for planning"></div></div>
        <div class="skill-tile" style="left:300px;top:163px;width:100px;height:94px"><div class="skill-art" role="img" aria-label="Software box icon for digital products"></div></div>
        <div class="skill-tile" style="left:441px;top:137px;width:100px;height:98px"><div class="skill-art" role="img" aria-label="Web page window icon for websites"></div></div>
        <div class="skill-tile" style="left:72px;top:262px;width:100px;height:98px"><div class="skill-art" role="img" aria-label="Browser window icon for online marketing"></div></div>
        <div class="skill-tile" style="left:230px;top:235px;width:150px;height:104px"><div class="skill-art" role="img" aria-label="Floppy disk and colour shapes icons for graphic design"></div></div>
        <div class="skill-tile" style="left:448px;top:235px;width:137px;height:105px"><div class="skill-art" role="img" aria-label="Colour swatch fan and image window icons for photography"></div></div>
        <div class="tile-reflection" style="left:55px"></div>
        <div class="tile-reflection" style="left:215px"></div>
        <div class="tile-reflection" style="left:430px"></div>
        <p class="series-name">Earn From Home Collection</p>
      </section>
      <footer class="author-band">Gerald Whitcombe</footer>
    </article>
  </main>
</body>
</html>
```